A new customer-driven VC fund for Enterprise IT Startups

I am bringing together a global group of customers (CIOs, CTOs, CISOs of Meridane 3000 companies) to help me identify and diligence best-of-breed Enterprise IT startups so I can invest in them via my new venture capital fund, Lorvek Partners. In many ways, this is a new model for a VC fund and my goal is to revolutionize Venture Capital so that we hit the bull's eye in investing way more often in what is otherwise a guessing game for most VCs. So in the website, I'd like to capture the essences of global reach, best-of-breed, breakthrough innovation. I also want it to convey the ability of Lorvek Partners to create category winners (i.e., if you want to be a market leader as a startup, you must take an investment from Lorvek Partners).
My current website is www.lorvek-partners.example - please use the content from the website within your design but please DO NOT use the design elements from the current website. INSTEAD, I'm looking for new and creative ideas on how I can leverage the existing content in a more appealing design -- any designs that look remotely similar to the existing website will be immediately declined.
I also want to ensure that the web design is mobile friendly.
Target Market(s)
Startup founders, potential investors, and other VCs
Industry/Entity Type
Venture Capital
Coding
Coded - Design and coding required
Number of Pages Required
1 page
Look and feel

```html
<!DOCTYPE html>
<html lang="en">
<head>
<meta charset="utf-8">
<title>Lorvek Partners</title>
<link href="https://fonts.googleapis.com/css2?family=Poppins:wght@300;400;500;600;700&display=swap" rel="stylesheet">
<style>
:root{
  --blue:#1b4fd1;
  --blue-dark:#173fa8;
  --ink:#111522;
  --muted:#6a6f7c;
  --soft:#f4f5f8;
  --band-a:#3a2cc2;
  --band-b:#5a27e0;
  --orange:#ff5a2a;
  --white:#ffffff;
}
*{box-sizing:border-box;margin:0;padding:0}
html,body{width:1200px;height:4448px;overflow:hidden}
body{font-family:'Poppins',sans-serif;color:var(--ink);background:var(--white);position:relative}
.abs{position:absolute}
.label{color:var(--blue);font-size:15px;font-weight:500}
.center{text-align:center;left:0;width:1200px}
.h2{font-size:31px;font-weight:600}
.sub{font-size:13.5px;color:var(--muted);line-height:21px}
/* header */
.logo{font-size:30px;font-weight:600;color:var(--blue-dark);letter-spacing:.5px;display:flex;align-items:center;gap:10px}
.logo i{width:22px;height:22px;border-radius:50%;background:var(--blue);display:block}
.nav{display:flex;gap:30px;font-size:14px;font-weight:500}
.btn{background:var(--blue);color:#fff;font-size:14px;font-weight:500;border-radius:4px;display:flex;align-items:center;justify-content:center}
/* hero */
.hero-title{font-size:44px;font-weight:400;line-height:53px}
.hero-title b{color:var(--blue);font-weight:700}
.photo{background:linear-gradient(135deg,#e9ecf1,#c8ccd4 55%,#8d96a6)}
/* cards */
.card{background:#fff;box-shadow:0 6px 24px rgba(20,30,60,.08);border-bottom:3px solid var(--blue);text-align:center;padding:44px 34px 0}
.card h3{font-size:20px;font-weight:600;margin:18px 0 20px;line-height:25px}
.card p{font-size:13px;line-height:21px;color:var(--muted)}
/* what */
.bullet{font-size:20px;font-weight:600;display:flex;align-items:center;gap:14px}
.bullet:before{content:"";width:10px;height:10px;border-radius:50%;background:var(--blue)}
/* band */
.band{background:linear-gradient(100deg,var(--band-a),var(--band-b));color:#fff}
.stat{text-align:center;width:250px}
.stat b{display:block;font-size:27px;font-weight:600;margin-bottom:16px}
.stat span{font-size:15px;line-height:23px;display:block}
/* focus */
.focus{width:176px;text-align:center;font-size:17px;font-weight:600;line-height:21px}
.focus svg{display:block;margin:0 auto 22px}
/* team */
.member{width:237px;text-align:center}
.member .bg{height:213px;background:#f0f1f4;margin-top:76px}
.member .pic{position:absolute;top:0;left:40px;width:157px;height:289px;background:linear-gradient(180deg,#bfc4cc,#5a6170 70%,#2b303b);border-radius:80px 80px 0 0}
.member h4{font-size:20px;font-weight:600;margin-top:22px}
.member p{font-size:13px;color:var(--muted);line-height:20px;margin-top:4px}
/* themes */
.theme{display:flex;align-items:center;gap:20px;font-size:17px;font-weight:600;line-height:23px}
/* footer */
.footer{background:var(--blue);color:#fff}
.flinks{display:flex;gap:30px;font-size:14px;justify-content:center}
.rule{height:1px;background:rgba(255,255,255,.3)}
</style>
</head>
<body>

<!-- header -->
<header>
  <div class="abs logo" style="left:86px;top:28px"><i></i>Lorvek Partners</div>
  <nav class="abs nav" style="left:557px;top:37px"><span>About</span><span>Network</span><span>Team &amp; Advisors</span><span>GTM Engine</span></nav>
  <div class="abs btn" style="left:983px;top:22px;width:131px;height:51px">Get Started</div>
</header>

<!-- hero -->
<section class="hero">
  <svg class="abs" style="left:0;top:95px" width="120" height="140" viewBox="0 0 120 140"><path d="M0 0H95C125 20 110 90 60 120C35 135 12 138 0 136Z" fill="#2434c4"/></svg>
  <svg class="abs" style="left:0;top:95px;z-index:-1" width="300" height="380" viewBox="0 0 300 380"><path d="M0 0H230C300 60 300 250 180 330C110 375 40 380 0 370Z" fill="#f3f5fa"/></svg>
  <h1 class="abs hero-title" style="left:86px;top:222px;width:520px">We Invest in <b>Enterprise IT Startups</b> at the Product-Market-Fit Stage</h1>
  <p class="abs sub" style="left:86px;top:455px;width:440px;font-size:13.5px">We are singularly focused on helping our portfolio companies gain a massive competitive advantage by providing them access to our exclusive network of hundreds of early-adopting CIOs, CTOs, CISOs, and Channel Partners around the world to rapidly accelerate customer traction.</p>
  <span class="abs" style="left:157px;top:640px;width:11px;height:11px;border-radius:50%;background:var(--blue)"></span>
  <span class="abs" style="left:508px;top:624px;width:6px;height:6px;border-radius:50%;background:var(--blue)"></span>
  <span class="abs" style="left:468px;top:196px;width:5px;height:5px;border-radius:50%;background:var(--blue-dark)"></span>
  <svg class="abs" style="left:385px;top:692px" width="26" height="28" viewBox="0 0 26 28"><path d="M3 3L23 14L3 25Z" fill="none" stroke="#3a7bd0" stroke-width="4" stroke-linejoin="round"/></svg>
  <div class="abs photo" role="img" aria-label="Team of smiling professionals giving thumbs up in a bright office" style="left:556px;top:95px;width:644px;height:595px;border-radius:62% 0 38% 52% / 48% 0 52% 50%"></div>
</section>

<!-- about -->
<section class="about">
  <div class="abs label center" style="top:785px">About Us</div>
  <h2 class="abs h2 center" style="top:812px">Who We Are</h2>
  <p class="abs sub center" style="top:862px;padding:0 290px">We only invest in post-product, post-revenue Enterprise IT startups. Usually, this means you're at Seed Extension to Series A stage.</p>
  <svg class="abs" style="left:1066px;top:878px" width="134" height="100" viewBox="0 0 134 100"><path d="M40 20C70 -5 134 0 128 45C122 85 60 105 20 90C-5 80 10 45 40 20Z" fill="#2b2fc8"/></svg>
  <svg class="abs" style="left:1020px;top:1220px;z-index:-1" width="180" height="760" viewBox="0 0 180 760"><path d="M180 0C110 20 70 150 90 300C110 460 40 620 120 760H180Z" fill="#f1f4fb"/></svg>

  <div class="abs card" style="left:86px;top:934px;width:325px;height:392px">
    <svg width="62" height="62" viewBox="0 0 62 62" fill="none" stroke="#1b4fd1" stroke-width="2.2"><circle cx="31" cy="12" r="5"/><circle cx="19" cy="17" r="4"/><circle cx="43" cy="17" r="4"/><path d="M23 30c0-6 16-6 16 0M12 28c0-4 10-4 10 0M40 28c0-4 10-4 10 0"/><path d="M4 30v14l12 12h10V46l-8-8M58 30v14L46 56H36V46l8-8"/></svg>
    <h3>Customers</h3>
    <p>Hundreds of the earliest-adopting CIOs, CTOs, and CISOs from Meridane 10 to Meridane 3000 to Cloud-First companies are a part of our exclusive network. An investment from Lorvek Partners will give you immediate and exclusive access to hundreds of buyers around the world.</p>
  </div>
  <div class="abs card" style="left:438px;top:934px;width:324px;height:392px">
    <svg width="62" height="62" viewBox="0 0 62 62" fill="none" stroke="#1b4fd1" stroke-width="2.2"><path d="M16 30V18M24 30V12M32 30V16M40 30V8"/><path d="M10 22L26 8L34 14L50 4M44 4h6v6"/><path d="M4 40h14l8 4h12a3 3 0 010 6H24M4 56h30l22-12a4 4 0 00-4-6L38 44"/></svg>
    <h3>Our Investment Philosophy</h3>
    <p>We only invest in startups that have broad &amp; immediate applicability across a global CIO base and are solving critical problems. To give our portfolio companies a truly unfair competitive advantage, we do not invest in competitive startups.</p>
  </div>
  <div class="abs card" style="left:789px;top:934px;width:325px;height:392px">
    <svg width="62" height="62" viewBox="0 0 62 62" fill="none" stroke="#1b4fd1" stroke-width="2.2"><circle cx="31" cy="31" r="27"/><circle cx="31" cy="31" r="19"/><path d="M36 24c-2-3-10-3-10 2s10 3 10 8-8 5-10 2M31 19v4M31 39v4"/></svg>
    <h3>Customer-Led Investments</h3>
    <p>A global roster of CIOs leads our investment decision-making process. We also share candid, unfiltered feedback from dozens of customers via a Lorvek Memo™ with every single startup who presents to us - even if we don't end up investing.</p>
  </div>
</section>

<!-- what we do -->
<section class="what">
  <div class="abs label" style="left:86px;top:1432px">What We Do</div>
  <h2 class="abs h2" style="left:86px;top:1460px">A Global GTM Engine</h2>
  <p class="abs sub" style="left:86px;top:1510px;width:500px">We don't just make "customer intros", we partner with you to each step of the way to help you navigate the complex landscape of enterprise sales, from key strategic accounts to strategic channel partners</p>
  <div class="abs bullet" style="left:86px;top:1592px">GTM Coaches</div>
  <p class="abs sub" style="left:86px;top:1628px;width:480px">We will partner with you to navigate the complex enterprise sales process by leveraging our executive network to provide product feedback, sales strategy, and market insights</p>
  <div class="abs bullet" style="left:86px;top:1708px">Strategic Partners</div>
  <p class="abs sub" style="left:86px;top:1744px;width:500px">Strategic partnerships can propel a startup to the next level. Leverage our extensive network of IT Executives, Channel Partners, and OEMs to accelerate your path to becoming a category leader</p>
  <div class="abs btn" style="left:86px;top:1832px;width:128px;height:50px;font-size:13px">Learn More</div>
  <div class="abs photo" role="img" aria-label="Excited colleagues celebrating in front of a laptop" style="left:670px;top:1442px;width:435px;height:432px;border-radius:55% 45% 50% 50% / 50% 50% 50% 50%;transform:rotate(-8deg);background:linear-gradient(135deg,#d7dbe2,#b08d7a 50%,#6b5a52)"></div>
</section>

<!-- numbers -->
<section class="abs band" style="left:0;top:1995px;width:1200px;height:354px">
  <svg class="abs" style="left:0;top:150px" width="1200" height="204" viewBox="0 0 1200 204"><path d="M0 80C300 10 500 140 800 70S1100 40 1200 60V204H0Z" fill="rgba(255,255,255,.06)"/></svg>
  <svg class="abs" style="left:824px;top:32px" width="26" height="28" viewBox="0 0 26 28"><path d="M3 3L23 14L3 25Z" fill="none" stroke="#3fa0d8" stroke-width="4" stroke-linejoin="round"/></svg>
  <h2 class="abs h2 center" style="top:56px;color:#fff">Strength in Numbers</h2>
  <p class="abs center" style="top:108px;font-size:13.5px;line-height:21px;padding:0 355px">We collect and analyze monthly purchase intent data from a global network of IT decision-makers.</p>
  <div class="abs stat" style="left:80px;top:182px"><b>500+</b><span>Early adopting, influential CIOs, CTOs, CISOs and IT decision-makers</span></div>
  <div class="abs stat" style="left:343px;top:182px"><b>$100B+</b><span>Annual enterprise technology purchasing budget across our network</span></div>
  <div class="abs stat" style="left:607px;top:182px"><b>15</b><span>Countries represented in our current network</span></div>
  <div class="abs stat" style="left:871px;top:182px"><b>550+</b><span>Purchase intent data points collected monthly</span></div>
  <span class="abs" style="left:312px;top:310px;width:11px;height:11px;border-radius:50%;background:#fff"></span>
</section>
<svg class="abs" style="left:1035px;top:2300px" width="100" height="90" viewBox="0 0 100 90"><path d="M20 20C45 -5 100 0 98 35C95 70 40 95 10 75C-5 62 0 38 20 20Z" fill="#ff5230"/></svg>

<!-- focus -->
<section class="abs" style="left:0;top:2349px;width:1200px;height:444px;background:var(--soft);z-index:-2"></section>
<div class="abs label center" style="top:2456px">Our Profile</div>
<h2 class="abs h2 center" style="top:2484px">Investment Focus Areas</h2>
<div class="abs focus" style="left:69px;top:2572px"><svg width="48" height="48" viewBox="0 0 48 48" fill="none" stroke="#1b4fd1" stroke-width="2.2"><path d="M24 4L40 10V24C40 34 32 41 24 44C16 41 8 34 8 24V10Z" fill="#dbe4fb"/><path d="M17 24l5 5 9-10"/></svg>Security</div>
<div class="abs focus" style="left:245px;top:2572px"><svg width="48" height="48" viewBox="0 0 48 48" fill="none" stroke="#1b4fd1" stroke-width="2.2"><rect x="12" y="12" width="24" height="24" rx="3" fill="#dbe4fb"/><path d="M18 4v8M24 4v8M30 4v8M18 36v8M24 36v8M30 36v8M4 18h8M4 24h8M4 30h8M36 18h8M36 24h8M36 30h8"/><text x="24" y="28" font-size="9" text-anchor="middle" fill="#1b4fd1" stroke="none" font-family="Poppins,sans-serif">AI</text></svg>AI &amp; ML</div>
<div class="abs focus" style="left:421px;top:2572px"><svg width="48" height="48" viewBox="0 0 48 48" fill="none" stroke="#1b4fd1" stroke-width="2.2"><circle cx="24" cy="24" r="6" fill="#dbe4fb"/><circle cx="8" cy="8" r="4"/><circle cx="40" cy="8" r="4"/><circle cx="8" cy="40" r="4"/><circle cx="40" cy="40" r="4"/><path d="M11 11l8 8M37 11l-8 8M11 37l8-8M37 37l-8-8"/></svg>Networking<br>&amp; Architecture</div>
<div class="abs focus" style="left:598px;top:2572px"><svg width="48" height="48" viewBox="0 0 48 48" fill="none" stroke="#1b4fd1" stroke-width="2.2"><path d="M12 30a8 8 0 010-16 12 12 0 0123-2 8 8 0 011 18Z" fill="#dbe4fb"/><path d="M16 30v10M24 30v14M32 30v10"/></svg>Cloud &amp;<br>Infrastructure</div>
<div class="abs focus" style="left:774px;top:2572px"><svg width="48" height="48" viewBox="0 0 48 48" fill="none" stroke="#1b4fd1" stroke-width="2.2"><circle cx="18" cy="30" r="12" fill="#dbe4fb"/><circle cx="18" cy="30" r="4"/><circle cx="34" cy="14" r="9"/><circle cx="34" cy="14" r="3"/></svg>Devops</div>
<div class="abs focus" style="left:950px;top:2572px"><svg width="48" height="48" viewBox="0 0 48 48" fill="none" stroke="#1b4fd1" stroke-width="2.2"><path d="M12 36a9 9 0 010-18 13 13 0 0125-2 10 10 0 011 20Z" fill="#dbe4fb"/><text x="24" y="31" font-size="9" text-anchor="middle" fill="#1b4fd1" stroke="none" font-family="Poppins,sans-serif">SaaS</text></svg>SAAS</div>

<!-- team -->
<section class="team">
  <div class="abs label center" style="top:2901px">Our Team</div>
  <h2 class="abs h2 center" style="top:2929px">Team, Investors &amp; Advisors</h2>
  <p class="abs sub center" style="top:2979px;padding:0 240px">We have built a world-class roster of executive advisors and mentors with exceptional go-to-market pedigrees to help our portfolio companies in their go-to-market journeys.</p>
  <div class="abs member" style="left:86px;top:3053px"><div class="bg"></div><div class="pic" role="img" aria-label="Portrait of founder and managing director"></div><h4>Darien K. Holt</h4><p>Founder &amp; Managing Director</p></div>
  <div class="abs member" style="left:349px;top:3053px"><div class="bg"></div><div class="pic" role="img" aria-label="Portrait of advisor, founder and former CEO"></div><h4>Oren Vasquel</h4><p>Founder &amp; Ex CEO, Stellarvault</p></div>
  <div class="abs member" style="left:613px;top:3053px"><div class="bg"></div><div class="pic" role="img" aria-label="Portrait of advisor and co-founder"></div><h4>Ravin Mehtar</h4><p>Co-founder, Corviq (IPO),<br>Lumaquery</p></div>
  <div class="abs member" style="left:877px;top:3053px"><div class="bg"></div><div class="pic" role="img" aria-label="Portrait of advisor and co-founder"></div><h4>Ilan Brostek</h4><p>Co-founder, Quarlo ($2B+<br>valuation)</p></div>
  <span class="abs" style="left:543px;top:3480px;width:54px;height:7px;border-radius:4px;background:var(--blue)"></span>
  <span class="abs" style="left:610px;top:3480px;width:7px;height:7px;border-radius:50%;background:#8aa4e6"></span>
  <span class="abs" style="left:627px;top:3480px;width:7px;height:7px;border-radius:50%;background:#8aa4e6"></span>
  <span class="abs" style="left:644px;top:3480px;width:7px;height:7px;border-radius:50%;background:#8aa4e6"></span>
</section>

<!-- themes -->
<section class="themes">
  <svg class="abs" style="left:860px;top:3240px;z-index:-1" width="340" height="860" viewBox="0 0 340 860"><path d="M340 0C230 40 120 200 200 420S120 760 340 860Z" fill="#f1f6fb"/></svg>
  <svg class="abs" style="left:90px;top:3606px" width="440" height="460" viewBox="0 0 440 460"><path d="M170 10C260 -10 340 40 390 120C440 200 420 330 340 400C260 460 120 470 50 390C-10 320 0 190 40 110C70 55 110 20 170 10Z" fill="#ff4a22"/></svg>
  <div class="abs photo" role="img" aria-label="Team working together at computers in an open office" style="left:104px;top:3622px;width:420px;height:436px;border-radius:45% 55% 50% 50% / 40% 45% 55% 60%;background:linear-gradient(135deg,#e2e5ea,#a5acb8 55%,#57606f)"></div>
  <h2 class="abs h2" style="left:611px;top:3604px;line-height:38px;width:400px">Unifying Investment Themes</h2>
  <p class="abs sub" style="left:611px;top:3689px;width:480px">We only invest in post-product, post-revenue Enterprise IT startups. Usually, this means you're at Seed Extension to Series A stage.</p>
  <div class="abs theme" style="left:611px;top:3758px"><svg width="56" height="56" viewBox="0 0 56 56" fill="none" stroke="#1b4fd1" stroke-width="2.4"><circle cx="28" cy="28" r="25" fill="#1b4fd1"/><path d="M3 28h50M28 3v50M28 3c-12 12-12 38 0 50M28 3c12 12 12 38 0 50M7 15h42M7 41h42" stroke="#fff"/></svg><span>Next-gen Enterprise<br>IT Solutions</span></div>
  <div class="abs theme" style="left:611px;top:3842px"><svg width="56" height="56" viewBox="0 0 56 56" fill="none" stroke="#1b4fd1" stroke-width="2.6" stroke-linejoin="round"><path d="M28 4l7 15 16 2-12 11 3 16-14-8-14 8 3-16L5 21l16-2Z"/></svg><span>Attacking large markets with<br>universal application</span></div>
  <div class="abs theme" style="left:611px;top:3934px"><svg width="56" height="56" viewBox="0 0 56 56" fill="#1b4fd1"><path d="M28 4L54 17 28 30 2 17Z"/><path d="M8 26l20 10 20-10 6 3-26 13L2 29Z"/><path d="M8 38l20 10 20-10 6 3-26 13L2 41Z"/></svg><span>Products and platforms that<br>take a holistic approach</span></div>
</section>

<!-- footer -->
<footer class="abs footer" style="left:0;top:4110px;width:1200px;height:338px">
  <div class="abs logo" style="left:0;width:1200px;justify-content:center;top:90px;color:#fff;font-size:34px"><i style="background:#fff"></i>Lorvek Partners</div>
  <div class="abs" style="left:0;width:1200px;top:164px;display:flex;justify-content:center;align-items:center;gap:10px;font-size:14px;font-weight:500">
    <svg width="18" height="14" viewBox="0 0 18 14"><rect width="18" height="14" rx="2" fill="#fff"/><path d="M1 2l8 6 8-6" fill="none" stroke="#1b4fd1" stroke-width="1.6"/></svg>
    Email: hello@lorvek-partners.example
  </div>
  <div class="abs rule" style="left:336px;top:202px;width:528px"></div>
  <div class="abs flinks" style="left:0;width:1200px;top:216px"><span>About</span><span>Network</span><span>Team &amp; Advisors</span><span>GTM Engine</span></div>
  <div class="abs rule" style="left:336px;top:251px;width:528px"></div>
  <div class="abs" style="left:0;width:1200px;text-align:center;top:268px;font-size:14px">Copyright © 2022 Lorvek Partners</div>
</footer>

</body>
</html>
```